Letterhead to Introduce a 'Sister' Company.

What I am needing is a design for a letter head to introduce our current customers base of (KT Alarm) customers to our new service, 'Kestrel Tide Solar Brokers'

```html
<!DOCTYPE html>
<html lang="en">
<head>
<meta charset="utf-8">
<title>Kestrel Tide Solar Brokers – Letterhead</title>
<link href="https://fonts.googleapis.com/css2?family=Lato:wght@400;700&family=Great+Vibes&display=swap" rel="stylesheet">
<style>
  :root {
    --navy: #122e52;
    --brand-blue: #1d4a86;
    --orange: #f49c1f;
    --ink: #555555;
    --ink-dark: #444444;
    --backdrop: #f3f3f3;
    --paper: #ffffff;
  }
  * { margin: 0; padding: 0; box-sizing: border-box; }
  html, body {
    width: 1018px; height: 1200px; overflow: hidden;
    background: var(--backdrop);
    font-family: "Lato", sans-serif;
  }
  .letterhead {
    position: absolute; left: 163px; top: 117px;
    width: 689px; height: 968px;
    background: var(--paper);
    overflow: hidden;
  }
  .header-band { position: absolute; left: 0; top: 0; width: 689px; height: 170px; }
  .contact {
    position: absolute; right: 62px; top: 25px;
    text-align: right; color: #fff; font-size: 13.5px; line-height: 17px;
    font-style: normal;
  }
  .contact .address { margin-bottom: 8px; }
  .contact .row { display: flex; justify-content: flex-end; align-items: center; gap: 6px; }
  .contact .label { color: var(--orange); }
  .contact svg { width: 12px; height: 12px; flex: none; }
  .brand {
    position: absolute; left: 66px; top: 122px;
    display: flex; align-items: center; gap: 10px;
  }
  .brand-dot { width: 22px; height: 22px; border-radius: 50%; background: var(--orange); }
  .brand-name {
    color: var(--brand-blue); font-weight: 700; font-size: 22px; line-height: 25px;
    letter-spacing: 0.5px; text-transform: uppercase;
  }
  .letter { position: absolute; left: 67px; top: 254px; width: 566px; color: var(--ink); }
  .date { font-size: 15.5px; }
  .recipient-name { margin-top: 16px; color: var(--orange); font-size: 17px; font-weight: 700; }
  .recipient-title { font-size: 15.5px; margin-top: 1px; }
  .recipient-address { margin-top: 22px; font-size: 15.5px; line-height: 19px; }
  .salutation { margin-top: 23px; font-size: 15.5px; font-weight: 700; color: var(--ink-dark); }
  .body p { margin-top: 14px; font-size: 13.2px; line-height: 16.2px; }
  .body p:first-child { margin-top: 22px; }
  .closing { margin-top: 33px; font-size: 15.5px; }
  .signature {
    margin-top: 12px; font-family: "Great Vibes", cursive;
    font-size: 42px; color: #222; line-height: 1;
  }
</style>
</head>
<body>
  <main class="letterhead">
    <svg class="header-band" viewBox="0 0 689 170" aria-hidden="true">
      <path d="M0,0 H689 V150 C500,170 260,70 0,45 Z" fill="var(--navy)"/>
    </svg>

    <address class="contact">
      <div class="address">2870 Harlow Avenue<br>Dublin, GA 31021</div>
      <div class="row">478.555.0143
        <svg viewBox="0 0 12 12"><path d="M1,5 Q6,1 11,5 L10,6.5 L8,5.5 V4.5 H4 V5.5 L2,6.5 Z M3,7 H9 L10,11 H2 Z" fill="var(--orange)"/></svg></div>
      <div class="row"><span><span class="label">(Fax)</span>478.555.0144</span>
        <svg viewBox="0 0 12 12"><rect x="3" y="1" width="6" height="4" fill="none" stroke="var(--orange)" stroke-width="1.2"/><rect x="1" y="5" width="10" height="4" rx="1" fill="var(--orange)"/><rect x="3" y="8" width="6" height="3" fill="none" stroke="var(--orange)" stroke-width="1.2"/></svg></div>
      <div class="row">kestreltide@mail.com
        <svg viewBox="0 0 12 12"><rect x="1" y="2.5" width="10" height="7" fill="var(--orange)"/><path d="M1,2.5 L6,6.5 L11,2.5" fill="none" stroke="var(--navy)" stroke-width="1"/></svg></div>
      <div class="row">www.kestreltide.com
        <svg viewBox="0 0 12 12"><circle cx="6" cy="6" r="5" fill="var(--orange)"/><path d="M1,6 H11 M6,1 Q3,6 6,11 M6,1 Q9,6 6,11" fill="none" stroke="var(--navy)" stroke-width="0.8"/></svg></div>
    </address>

    <div class="brand">
      <span class="brand-dot" aria-hidden="true"></span>
      <span class="brand-name">Kestrel Tide<br>Solar Brokers</span>
    </div>

    <article class="letter">
      <p class="date">September 21-2020</p>
      <p class="recipient-name">MR. ALAN REEVE</p>
      <p class="recipient-title">President</p>
      <p class="recipient-address">2870 Harlow Avenue<br>Dublin, GA 31021</p>
      <p class="salutation">Dear Mr, Alan</p>
      <div class="body">
        <p>This is a sample version of Lorem Ipsum. Proin gravida nibh vel velit auctor aliquet. Aenean sollicitudin, lorem quis bibendum auctor, nisi elit consequat ipsum, nec sagittis sem nibh id elit. Duis sed odio sit amet nibh vulputate cursus a sit amet mauris. Morbi accumsan ipsum velit. Nam nec tellus a odio tincidunt auctor a ornare odio. Sed non mauris elit.</p>
        <p>This is a sample version of Lorem Ipsum. Proin gravida nibh vel velit auctor aliquet. Aenean sollicitudin, lorem quis bibendum auctor, nisi elit consequat ipsum, nec sagittis sem nibh id elit. Duis sed odio sit amet nibh vulputate cursus a sit amet mauris. Morbi accumsan ipsum velit. Nam nec tellus a odio tincidunt auctor a ornare odio. Sed non mauris elit.</p>
        <p>This is a sample version of Lorem Ipsum. Proin gravida nibh vel velit auctor aliquet. Aenean sollicitudin, lorem quis bibendum auctor, nisi elit consequat ipsum, nec sagittis sem nibh id elit. Duis sed odio sit amet nibh vulputate cursus a sit amet mauris.</p>
        <p>This is a sample version of Lorem Ipsum. Proin gravida nibh vel velit auctor aliquet. Aenean sollicitudin, lorem quis bibendum auctor, nisi elit consequat ipsum.</p>
      </div>
      <p class="closing">Regard</p>
      <p class="signature">Mark Halden</p>
    </article>
  </main>
</body>
</html>
```